BUSINESS CARD DESIGN

NAME- TODD MASVERIK
PHONE NUMER - 808- 451-7082
EMAIL- OFFICE@VORLINDE-GRADEWAY.COM
BACK OF CARD- SPEACIALIZES IN LAND CLEARING, FORESTRY MUCLHING AND EXCAVATION

Contact Information for Business Card

NAME- TODD MASVERIK PHONE NUMER - 808- 451-7082 EMAIL- OFFICE@VORLINDE-GRADEWAY.COM BACK OF CARD- SPEACIALIZES IN LAND CLEARING , MUCLHING AND EXCAVATION

```html
<!DOCTYPE html>
<html lang="en">
<head>
<meta charset="utf-8">
<title>Business Card – Todd Masverik</title>
<link href="https://fonts.googleapis.com/css2?family=Montserrat:wght@400;500;700&display=swap" rel="stylesheet">
<style>
  :root {
    --backdrop: #1d1d1d;
    --card: #f4f4f4;
    --ink: #262626;
    --ink-soft: #3a3a3a;
  }
  * { margin: 0; padding: 0; box-sizing: border-box; }
  html, body {
    width: 1200px; height: 1059px; overflow: hidden;
    background: var(--backdrop);
    font-family: "Montserrat", sans-serif;
    color: var(--ink);
  }
  .canvas { position: relative; width: 1200px; height: 1059px; }
  .card {
    position: absolute;
    width: 690px; height: 392px;
    background: var(--card);
    border-radius: 16px;
  }
  .card--front { left: 256px; top: 89px; }
  .card--back  { left: 255px; top: 546px; }

  .identity {
    position: absolute; right: 412px; top: 176px;
    text-align: right;
  }
  .identity__name {
    font-weight: 700; font-size: 28px; letter-spacing: 0.5px; line-height: 1;
  }
  .identity__role {
    font-weight: 400; font-size: 15px; letter-spacing: 1px; margin-top: 6px; line-height: 1;
    color: var(--ink-soft);
  }
  .divider {
    position: absolute; left: 297px; top: 167px;
    width: 1.5px; height: 69px; background: var(--ink);
  }
  .contact {
    position: absolute; left: 322px; top: 163px;
    list-style: none;
  }
  .contact__item {
    display: flex; align-items: center; gap: 6px;
    font-size: 16.5px; font-weight: 400; letter-spacing: 0.6px;
    height: 28.5px; color: var(--ink-soft);
  }
  .contact__icon { width: 11px; height: 11px; flex: none; }

  .tagline {
    position: absolute; left: 0; right: 0; top: 160px;
    text-align: center;
    font-weight: 500; font-size: 27px; letter-spacing: 1.2px; line-height: 47px;
  }
</style>
</head>
<body>
<main class="canvas">
  <section class="card card--front" aria-label="Card front">
    <div class="identity">
      <p class="identity__name">TODD MASVERIK</p>
      <p class="identity__role">DIRECTOR</p>
    </div>
    <div class="divider"></div>
    <ul class="contact">
      <li class="contact__item">
        <svg class="contact__icon" viewBox="0 0 12 12" aria-hidden="true"><path fill="#262626" d="M1 4c0-2 2-3 5-3s5 1 5 3v1H8V4H4v1H1zM2.5 6h7l1 5h-9z"/></svg>
        808- 451-7082
      </li>
      <li class="contact__item">
        <svg class="contact__icon" viewBox="0 0 12 12" aria-hidden="true"><path fill="#262626" d="M1 5l5-4 5 4v6H1z"/><path fill="none" stroke="#f4f4f4" stroke-width="1" d="M1.5 5.5L6 8.5l4.5-3"/></svg>
        OFFICE@VORLINDE-GRADEWAY.COM
      </li>
      <li class="contact__item">
        <svg class="contact__icon" viewBox="0 0 12 12" aria-hidden="true"><circle cx="6" cy="6" r="5.5" fill="#262626"/><path fill="#f4f4f4" d="M3 3.5l2 .5 .5 2-1.5 1 .5 2L3 8zM7.5 2.5l1.5 1-1 1.5z"/></svg>
        WWW.VORLINDE-GRADEWAY.COM
      </li>
    </ul>
  </section>

  <section class="card card--back" aria-label="Card back">
    <p class="tagline">SPEACIALIZES IN LAND CLEARING<br>MUCLHING AND EXCAVATION</p>
  </section>
</main>
</body>
</html>
```